A Billboard Sign - TWO SIGNS

Hi, I’m looking to produce approximately 2.74 m by 2.74 m for a billboard-style display. I have a mock-up of the general look and feel, but I need a more polished, professional design. The sign will be viewed by people driving past, so the messaging must be clear, bold and easily readable at speed.

I also need a second sign sized 1 m by 3 m, following the same branding and visual style as the larger piece.

Requirements
Must have
• It must use the colours I've submitted
Nice to have
• I would like to see some good ideas in the general theme of what I have Mocked up. I don't the same design sent back to me

```html
<!DOCTYPE html>
<html lang="en">
<head>
<meta charset="utf-8">
<title>Insightful Ventures – Billboard Signs</title>
<link rel="stylesheet" href="https://fonts.googleapis.com/css2?family=Montserrat:wght@800&family=Poppins:wght@600;700&family=Roboto:wght@500;700&display=swap">
<style>
  :root {
    --navy: #1e2d36;
    --amber: #ffa400;
    --paper: #ffffff;
    --mist: #e1e1e1;
    --stage: #adadad;
    --ink: #151515;
    --partner-red: #e3262b;
    --partner-grey: #6f6f6f;
  }
  * { margin: 0; padding: 0; box-sizing: border-box; }
  html, body { width: 875px; height: 1200px; overflow: hidden; background: var(--stage); }
  .canvas { position: relative; width: 875px; height: 1200px; }
  .abs { position: absolute; }

  /* ---------- square sign ---------- */
  .sign-square {
    position: absolute; left: 147px; top: 96px; width: 581px; height: 581px;
    background: var(--navy); overflow: hidden;
    box-shadow: 0 4px 12px rgba(0,0,0,.25);
  }
  .sign-square .brand-dot {
    left: 41px; top: 37px; width: 138px; height: 138px; border-radius: 50%;
    border: 20px solid var(--amber);
  }
  .sign-square .brand-name {
    left: 210px; top: 58px; font-family: 'Poppins', sans-serif; font-weight: 700;
    font-size: 46px; line-height: 50px; color: var(--amber); letter-spacing: .5px;
  }
  .headline-top {
    font-family: 'Montserrat', sans-serif; font-weight: 800; color: var(--mist);
    letter-spacing: 2px; white-space: nowrap;
  }
  .headline-main {
    font-family: 'Montserrat', sans-serif; font-weight: 800; color: var(--amber);
    white-space: nowrap;
  }
  .sign-square .headline-top { left: 0; width: 581px; text-align: center; top: 197px; font-size: 52px; line-height: 56px; }
  .sign-square .headline-main { left: 0; width: 581px; text-align: center; top: 243px; font-size: 58px; line-height: 62px; }
  .sign-square .role-pill {
    left: 44px; top: 311px; width: 493px; height: 45px; border-radius: 8px;
    background: var(--mist); color: var(--navy);
    font-family: 'Roboto', sans-serif; font-weight: 700; font-size: 33px;
    line-height: 45px; text-align: center;
  }
  .sign-square .footer-band {
    left: 0; top: 393px; width: 581px; height: 188px; background: var(--amber);
  }
  .partner-box {
    left: 35px; top: 30px; width: 510px; height: 66px; border-radius: 12px;
    background: var(--paper); overflow: hidden; display: flex;
  }
  .partner-box .partner-label {
    width: 258px; height: 100%; background: var(--navy); border-radius: 12px;
    color: var(--paper); font-family: 'Roboto', sans-serif; font-weight: 700;
    font-size: 23px; line-height: 26px; padding: 7px 0 0 16px;
  }
  .partner-names {
    flex: 1; display: flex; align-items: center; justify-content: space-evenly;
    font-family: 'Roboto', sans-serif; font-weight: 500;
  }
  .partner-a { color: var(--partner-red); letter-spacing: 1px; }
  .partner-b { color: var(--partner-grey); }
  .partner-box .partner-a, .partner-box .partner-b { font-size: 20px; }
  .sign-square .web-address {
    left: 0; top: 110px; width: 581px; text-align: center;
    font-family: 'Roboto', sans-serif; font-weight: 700; font-size: 32px; color: var(--paper);
  }

  .size-label {
    left: 0; width: 875px; text-align: center; font-family: 'Poppins', sans-serif;
    font-weight: 600; font-size: 35px; color: var(--ink);
  }

  /* ---------- wide sign ---------- */
  .sign-wide {
    position: absolute; left: 147px; top: 821px; width: 581px; height: 193px;
    background: var(--paper); overflow: hidden;
    box-shadow: 0 4px 12px rgba(0,0,0,.25);
  }
  .sign-wide .top-rule { left: 0; top: 0; width: 581px; height: 8px; background: var(--navy); }
  .sign-wide .top-accent { left: 0; top: 6px; width: 240px; height: 4px; background: var(--amber); }
  .sign-wide .headline-panel {
    left: 228px; top: 0; width: 353px; height: 106px; background: var(--navy);
    clip-path: polygon(0 0, 100% 0, 100% 100%, 22px 100%);
  }
  .sign-wide .headline-panel-edge {
    left: 232px; top: 6px; width: 10px; height: 100px; background: var(--amber);
    clip-path: polygon(0 0, 4px 0, 18px 100%, 14px 100%);
  }
  .sign-wide .role-strip {
    left: 250px; top: 75px; width: 331px; height: 31px; background: var(--amber);
    clip-path: polygon(0 0, 100% 0, 100% 100%, 6px 100%);
    color: var(--navy); font-family: 'Roboto', sans-serif; font-weight: 700;
    font-size: 21px; line-height: 31px; padding-left: 8px; white-space: nowrap;
  }
  .sign-wide .headline-top { left: 258px; top: 9px; font-size: 28px; line-height: 30px; letter-spacing: 1px; }
  .sign-wide .headline-main { left: 256px; top: 36px; font-size: 32px; line-height: 36px; }
  .sign-wide .brand-dot {
    left: 13px; top: 31px; width: 56px; height: 56px; border-radius: 50%;
    border: 9px solid var(--amber);
  }
  .sign-wide .brand-name {
    left: 83px; top: 36px; font-family: 'Poppins', sans-serif; font-weight: 700;
    font-size: 19px; line-height: 21px; color: var(--amber);
  }
  .sign-wide .partner-row {
    left: 15px; top: 106px; width: 556px; height: 52px; display: flex; align-items: center;
    font-family: 'Roboto', sans-serif;
  }
  .sign-wide .partner-row .partner-label { font-weight: 700; font-size: 19px; color: var(--ink); margin-right: 22px; }
  .sign-wide .partner-row .partner-a { font-size: 22px; margin-right: 30px; }
  .sign-wide .partner-row .partner-b { font-size: 22px; }
  .sign-wide .footer-dark { left: 0; top: 158px; width: 581px; height: 35px; background: var(--navy); }
  .sign-wide .footer-amber {
    left: 218px; top: 158px; width: 363px; height: 35px; background: var(--amber);
    clip-path: polygon(0 0, 100% 0, 100% 100%, 12px 100%);
  }
  .sign-wide .footer-cta {
    left: 13px; top: 158px; line-height: 35px; color: var(--paper);
    font-family: 'Roboto', sans-serif; font-weight: 700; font-size: 16px;
  }
  .sign-wide .web-address {
    right: 14px; top: 158px; line-height: 35px; color: var(--paper);
    font-family: 'Roboto', sans-serif; font-weight: 700; font-size: 20px;
  }
</style>
</head>
<body>
<main class="canvas">

  <section class="sign-square" aria-label="Square billboard sign">
    <div class="abs brand-dot"></div>
    <div class="abs brand-name">INSIGHTFUL<br>VENTURES</div>
    <div class="abs headline-top">AWARD WINNING</div>
    <div class="abs headline-main">DATA ANALYTICS</div>
    <div class="abs role-pill">IMPLEMENTATION PARTNER</div>
    <div class="abs footer-band">
      <div class="abs partner-box">
        <div class="partner-label">PROUDLY<br>PARTNERING WITH</div>
        <div class="partner-names">
          <span class="partner-a">ORBITAL</span>
          <span class="partner-b">Northsoft</span>
        </div>
      </div>
      <div class="abs web-address">www.insightful-ventures.com</div>
    </div>
  </section>
  <div class="abs size-label" style="top:705px;">2.74 m by 2.74 m</div>

  <section class="sign-wide" aria-label="Wide banner sign">
    <div class="abs top-rule"></div>
    <div class="abs top-accent"></div>
    <div class="abs brand-dot"></div>
    <div class="abs brand-name">INSIGHTFUL<br>VENTURES</div>
    <div class="abs headline-panel"></div>
    <div class="abs headline-panel-edge"></div>
    <div class="abs headline-top">AWARD WINNING</div>
    <div class="abs headline-main">DATA ANALYTICS</div>
    <div class="abs role-strip">IMPLEMENTATION PARTNER</div>
    <div class="abs partner-row">
      <span class="partner-label">PROUDLY PARTNERING WITH</span>
      <span class="partner-a">ORBITAL</span>
      <span class="partner-b">Northsoft</span>
    </div>
    <div class="abs footer-dark"></div>
    <div class="abs footer-amber"></div>
    <div class="abs footer-cta">VISIT US OUR WEBSITE</div>
    <div class="abs web-address">www.insightful-ventures.com</div>
  </section>
  <div class="abs size-label" style="top:1058px;">1 m by 3 m</div>

</main>
</body>
</html>
```